Tarnby Group letterhead

Hi,

I need a letterhead template created for our business. This should be done in word format and A4 size. The images need to not move in the template ie when I am adding writing in etc. and should flow on when I get to a second page.

I have attached our logo templates below.

Other details to include on the letterhead somewhere are:

0438 915 267
Max@Tarnbyelectrical.example.au
PO Box 817 Marrowvale NSW 2190
ABN: 57 318 962 407

Thanks!

```html
<!DOCTYPE html>
<html lang="en">
<head>
<meta charset="utf-8">
<title>Tarnby Group Letterhead</title>
<link href="https://fonts.googleapis.com/css2?family=Poppins:wght@400;700&display=swap" rel="stylesheet">
<style>
  :root {
    --orange: #f55200;
    --charcoal: #333333;
    --slate: #757575;
    --paper: #ffffff;
    --ink: #111111;
  }
  html, body {
    margin: 0;
    padding: 0;
    overflow: hidden;
    background: var(--paper);
  }
  .letterhead {
    position: relative;
    width: 848px;
    height: 1200px;
    overflow: hidden;
    background: var(--paper);
    font-family: "Poppins", sans-serif;
  }
  .corner-accent {
    position: absolute;
    display: block;
  }
  .corner-accent.is-top {
    top: 0;
    left: 0;
    width: 341px;
    height: 263px;
  }
  .corner-accent.is-bottom {
    right: 0;
    bottom: 0;
    width: 338px;
    height: 262px;
  }
  .stop-orange { stop-color: var(--orange); }
  .stop-slate { stop-color: var(--slate); }
  .stop-charcoal { stop-color: var(--charcoal); }

  .brand {
    position: absolute;
    top: 86px;
    left: 500px;
    width: 288px;
    text-align: center;
  }
  .brand-mark {
    display: block;
    width: 78px;
    height: 78px;
    margin: 0 auto 20px;
    border-radius: 50%;
    background: var(--charcoal);
  }
  .brand-name {
    margin: 0;
    font-size: 24px;
    font-weight: 700;
    letter-spacing: 1px;
    text-transform: uppercase;
    color: var(--charcoal);
    line-height: 1;
  }

  .contact-list {
    position: absolute;
    left: 85px;
    top: 1035px;
    margin: 0;
    padding: 0;
    list-style: none;
  }
  .contact-item {
    display: flex;
    align-items: center;
    height: 22px;
    margin-bottom: 9.7px;
    font-size: 14px;
    color: var(--ink);
  }
  .contact-icon {
    width: 22px;
    height: 22px;
    margin-right: 10px;
    flex: none;
  }
  .contact-icon.is-orange { background: var(--orange); }
  .contact-icon.is-slate { background: var(--slate); }
  .contact-icon svg { display: block; width: 22px; height: 22px; }
</style>
</head>
<body>
<div class="letterhead">
  <svg class="corner-accent is-top" viewBox="0 0 341 263" role="img" aria-label="Decorative corner pattern in orange, charcoal and grey">
    <defs>
      <linearGradient id="top-accent-fill" x1="1" y1="0" x2="0" y2="1">
        <stop offset="0" class="stop-orange"/>
        <stop offset="0.6" class="stop-slate"/>
        <stop offset="1" class="stop-charcoal"/>
      </linearGradient>
    </defs>
    <polygon points="0,0 341,0 0,263" fill="url(#top-accent-fill)"/>
  </svg>

  <svg class="corner-accent is-bottom" viewBox="0 0 338 262" role="img" aria-label="Decorative corner pattern in charcoal, grey and orange">
    <defs>
      <linearGradient id="bottom-accent-fill" x1="0" y1="1" x2="1" y2="0">
        <stop offset="0" class="stop-charcoal"/>
        <stop offset="0.4" class="stop-slate"/>
        <stop offset="1" class="stop-orange"/>
      </linearGradient>
    </defs>
    <polygon points="338,0 338,262 0,262" fill="url(#bottom-accent-fill)"/>
  </svg>

  <header class="brand">
    <span class="brand-mark"></span>
    <h1 class="brand-name">Tarnby Group</h1>
  </header>

  <ul class="contact-list">
    <li class="contact-item">
      <span class="contact-icon is-orange">
        <svg viewBox="0 0 22 22"><path d="M7.5 5.5c.8-.4 1.4 0 1.8.8l.8 1.6c.3.7.1 1.2-.4 1.6l-.6.4c.5 1.4 1.6 2.6 3 3.2l.5-.6c.4-.5 1-.6 1.6-.3l1.5.9c.7.4 1 1 .5 1.8-.7 1.1-1.8 1.5-3 1.1C9.9 15 7 12 6.2 8.8c-.3-1.300.2-2.6 1.3-3.3z" fill="none" stroke="#fff" stroke-width="1"/></svg>
      </span>
      0438 915 267
    </li>
    <li class="contact-item">
      <span class="contact-icon is-slate">
        <svg viewBox="0 0 22 22"><rect x="5.5" y="7" width="11" height="8" fill="#fff"/><path d="M5.5 7.3 11 11.3l5.5-4" fill="none" stroke="#757575" stroke-width="1"/></svg>
      </span>
      Max@Tarnbyelectrical.example.au
    </li>
    <li class="contact-item">
      <span class="contact-icon is-orange">
        <svg viewBox="0 0 22 22"><path d="M11 4.5a4.3 4.3 0 0 0-4.3 4.3c0 3.2 4.3 8.2 4.3 8.2s4.3-5 4.3-8.2A4.3 4.3 0 0 0 11 4.5z" fill="#fff"/><circle cx="11" cy="8.8" r="1.5" fill="#f55200"/></svg>
      </span>
      PO Box 817 Marrowvale NSW 2190
    </li>
    <li class="contact-item">
      <span class="contact-icon is-slate">
        <svg viewBox="0 0 22 22"><rect x="5" y="6" width="12" height="10.5" rx="1" fill="#fff" stroke="#111" stroke-width="0.8"/><path d="M5 9.5 11 13l6-3.5M5 7.8h12" fill="none" stroke="#111" stroke-width="0.8"/></svg>
      </span>
      ABN: 57 318 962 407
    </li>
  </ul>
</div>
</body>
</html>
```